Land Buying Company Needs Letterhead for Direct Mail Marketing to Land Owners

We are looking for a professional letterhead that we will be including in our direct mail marketing. We will be sending this to land owners who may be interested in selling or purchasing land.

The letterhead needs to be editable. Headers and footers would look nice, but we are open. We would want it to include our address, website, phone, and email info. For right now the address to use for design purposes would the following:

Address: 415 Bramwell Avenue #600
Dallas, TX 75219
Website - www.quillridgeacres.example
Email - info@quillridgeacres.example
Phone - 866-402-ACRE

I have attached our logo zip file that we just had done on Pixel Guild. Let me know what questions you have, and thank you.

```html
<!DOCTYPE html>
<html lang="en">
<head>
<meta charset="utf-8">
<title>Quill Ridge Acres Letterhead</title>
<link rel="stylesheet" href="https://fonts.googleapis.com/css2?family=Montserrat:wght@600&family=Fira+Sans:wght@600&display=swap">
<style>
  :root {
    --backdrop: #b1b3b2;
    --paper: #ffffff;
    --leaf-green: #a2c523;
    --forest-green: #4e6330;
    --ink: #231f20;
    --watermark: #f2f2f0;
  }
  html, body {
    margin: 0;
    padding: 0;
    width: 1200px;
    height: 1200px;
    overflow: hidden;
    background: var(--backdrop);
  }
  .letterhead {
    position: absolute;
    left: 294px;
    top: 204px;
    width: 612px;
    height: 792px;
    background: var(--paper);
    overflow: hidden;
  }
  .brand {
    position: absolute;
    left: 25px;
    top: 53px;
    display: flex;
    align-items: center;
    gap: 12px;
  }
  .brand-mark {
    width: 54px;
    height: 54px;
    border-radius: 50%;
    background: var(--forest-green);
  }
  .brand-name {
    font-family: "Montserrat", sans-serif;
    font-weight: 600;
    font-size: 27px;
    letter-spacing: 1px;
    color: var(--leaf-green);
    text-transform: uppercase;
    white-space: nowrap;
  }
  .contact {
    position: absolute;
    left: 415px;
    top: 34px;
    height: 92px;
    padding-left: 10px;
    border-left: 1.5px solid var(--leaf-green);
    font-family: "Fira Sans", sans-serif;
    font-weight: 600;
    color: var(--ink);
  }
  .address {
    margin: 3px 0 6px;
    font-size: 11.5px;
    line-height: 16px;
  }
  .contact-row {
    display: flex;
    align-items: center;
    height: 19px;
    font-size: 9.6px;
  }
  .contact-icon {
    width: 14px;
    height: 12px;
    margin-right: 12px;
    fill: none;
    stroke: var(--leaf-green);
    stroke-width: 1.4;
  }
  .contact-icon .solid { fill: var(--leaf-green); stroke: none; }
  .watermark {
    position: absolute;
    left: 143px;
    top: 235px;
    width: 326px;
    height: 326px;
    border-radius: 50%;
    background: var(--watermark);
  }
  .footer-bands {
    position: absolute;
    left: 0;
    bottom: 0;
    width: 612px;
    height: 30px;
  }
</style>
</head>
<body>
  <main class="letterhead">
    <header>
      <div class="brand">
        <div class="brand-mark"></div>
        <div class="brand-name">Quill Ridge Acres</div>
      </div>
      <address class="contact" style="font-style:normal">
        <div class="address">415 Bramwell Avenue #600<br>Dallas, TX 75219</div>
        <div class="contact-row">
          <svg class="contact-icon" viewBox="0 0 14 12" aria-hidden="true">
            <path class="solid" d="M1 3.5 C1 1 13 1 13 3.5 L13 4.5 L10 4.5 L10 3.5 L4 3.5 L4 4.5 L1 4.5 Z"/>
            <rect class="solid" x="3" y="5" width="8" height="6" rx="1"/>
          </svg>
          <span>866-402-ACRE</span>
        </div>
        <div class="contact-row">
          <svg class="contact-icon" viewBox="0 0 14 12" aria-hidden="true">
            <rect class="solid" x="0.5" y="2" width="13" height="8.5"/>
            <path d="M0.8 2.3 L7 7 L13.2 2.3 M0.8 10.3 L5.3 5.8 M13.2 10.3 L8.7 5.8" stroke="#fff" stroke-width="1"/>
          </svg>
          <span>info@quillridgeacres.example</span>
        </div>
        <div class="contact-row">
          <svg class="contact-icon" viewBox="0 0 14 12" aria-hidden="true">
            <circle cx="7" cy="6" r="5.2"/>
            <path d="M2 6 H12 M7 0.8 C4.5 3.5 4.5 8.5 7 11.2 M7 0.8 C9.5 3.5 9.5 8.5 7 11.2" stroke-width="1"/>
          </svg>
          <span>www.quillridgeacres.example</span>
        </div>
      </address>
    </header>

    <div class="watermark" aria-hidden="true"></div>

    <footer>
      <svg class="footer-bands" viewBox="0 0 612 30" aria-hidden="true">
        <polygon points="0,22 612,22 612,30 0,30" fill="var(--leaf-green)"/>
        <polygon points="470,0 612,0 612,30 456,30 456,20" fill="var(--leaf-green)"/>
        <polygon points="2,7 150,7 148,11.5 0,11.5" fill="var(--forest-green)"/>
        <polygon points="154,7 302,7 300,11.5 152,11.5" fill="var(--forest-green)"/>
        <polygon points="306,7 454,7 452,11.5 304,11.5" fill="var(--forest-green)"/>
      </svg>
    </footer>
  </main>
</body>
</html>
```